2018 Mother's Day and Baby Blessing poster

I need a poster Mother's Day and Baby Blessing ceremony for a Lantern Meadow Festival at Sydney Kestrel Quay. There is no specification on the design, however the only requirement is to present mother and baby in the poster. I would like the design to be modern, attractive and simple.

Must have:
Date: 13/5/2018 (Sunday)
Time: 2:00pm (1:00pm registration)
Venue: Merrowind Park, Kestrel Quay
Logo

```html
<!DOCTYPE html>
<html lang="en">
<head>
<meta charset="utf-8">
<title>Mother's Day &amp; Baby Blessing Ceremony</title>
<link href="https://fonts.googleapis.com/css2?family=Kaushan+Script&family=Oswald:wght@300;400&display=swap" rel="stylesheet">
<style>
  :root {
    --page: #e6e4e0;
    --paper: #f5f5f4;
    --sidebar: #58a892;
    --sidebar-text: #f3faf7;
    --title: #6b3518;
    --ceremony: #ee9422;
    --wreath-a: #eef6e6;
    --wreath-b: #cfe6bb;
    --skin-light: #f7e3d8;
    --skin: #e9b9a0;
    --hair: #8a4f2e;
    --hair-dark: #5e3018;
    --logo-ink: #2a2a2a;
    --logo-accent: #ef9a34;
  }
  html, body { margin: 0; padding: 0; overflow: hidden; }
  body {
    width: 1200px; height: 800px;
    background: var(--page);
    position: relative;
  }
  .poster {
    position: absolute; left: 330px; top: 18px;
    width: 540px; height: 764px;
    background: var(--paper);
    overflow: hidden;
    box-shadow: 0 2px 10px rgba(0,0,0,0.12);
  }
  .sidebar {
    position: absolute; left: 25px; top: 0;
    width: 116px; height: 490px;
    background: var(--sidebar);
    color: var(--sidebar-text);
    font-family: "Oswald", sans-serif;
    font-weight: 300;
  }
  .lotus {
    position: absolute; left: 22px; top: 54px;
    width: 72px; height: 58px;
    border-radius: 50% 50% 42% 42%;
    background: radial-gradient(circle at 50% 62%, #fbd6e1, #ea8dab 70%, rgba(234,141,171,0) 72%);
  }
  .details { position: absolute; left: 10px; top: 228px; width: 98px; }
  .detail { margin-bottom: 24px; }
  .detail:last-child { margin-bottom: 0; }
  .detail-label {
    display: flex; align-items: center; gap: 5px;
    font-size: 15px; font-weight: 400; text-transform: uppercase;
    padding-bottom: 4px; border-bottom: 1px solid var(--sidebar-text);
    margin-bottom: 7px;
  }
  .detail-label svg { width: 12px; height: 12px; }
  .detail-value { font-size: 15px; line-height: 1.35; }
  .detail-note { font-size: 11px; line-height: 1.35; }
  .wreath {
    position: absolute; left: 152px; top: 34px;
    width: 380px; height: 390px; border-radius: 50%;
    background: radial-gradient(circle, var(--paper) 52%, var(--wreath-b) 61%, var(--wreath-a) 68%, rgba(245,245,244,0) 71%);
  }
  .title {
    position: absolute; left: 150px; top: 130px; width: 390px;
    text-align: center; margin: 0;
    font-family: "Kaushan Script", cursive; font-weight: 400;
    color: var(--title); line-height: 1.08;
  }
  .title-line { display: block; font-size: 50px; }
  .title-amp { display: block; font-size: 40px; }
  .ceremony {
    position: absolute; left: 263px; top: 312px;
    width: 180px; height: 44px;
    background: var(--ceremony);
    transform: rotate(-4deg);
    color: #fff; text-align: center;
    font-family: "Kaushan Script", cursive;
    font-size: 32px; line-height: 44px;
  }
  .photo {
    position: absolute; left: 186px; top: 418px;
    width: 354px; height: 346px;
    background:
      radial-gradient(ellipse 40% 45% at 28% 42%, var(--skin-light) 0%, var(--skin-light) 55%, rgba(247,227,216,0) 100%),
      radial-gradient(ellipse 30% 35% at 58% 35%, var(--skin) 0%, rgba(233,185,160,0) 100%),
      radial-gradient(ellipse 45% 80% at 85% 40%, var(--hair) 0%, var(--hair-dark) 60%, rgba(94,48,24,0) 100%),
      radial-gradient(ellipse 55% 40% at 40% 85%, var(--skin) 0%, rgba(233,185,160,0) 100%),
      linear-gradient(100deg, var(--paper) 0%, var(--skin-light) 30%, var(--skin) 60%, var(--hair) 100%);
    -webkit-mask-image: linear-gradient(100deg, transparent 0%, #000 14%);
    mask-image: linear-gradient(100deg, transparent 0%, #000 14%);
  }
  .logo {
    position: absolute; left: 16px; top: 520px; width: 150px;
    display: flex; flex-direction: column; align-items: center; gap: 16px;
  }
  .logo-mark {
    width: 84px; height: 84px; border-radius: 50%;
    background: var(--logo-accent);
  }
  .logo-name {
    font-family: "Oswald", sans-serif; font-weight: 400;
    color: var(--logo-ink); font-size: 22px; line-height: 1.1;
    text-align: center; margin: 0;
  }
</style>
</head>
<body>
  <main class="poster">
    <aside class="sidebar">
      <div class="lotus" role="img" aria-label="Pink lotus flower illustration"></div>
      <div class="details">
        <div class="detail">
          <div class="detail-label">
            <svg viewBox="0 0 12 12" fill="none" stroke="currentColor" stroke-width="1.2"><rect x="1" y="2" width="10" height="9" rx="1"/><line x1="1" y1="5" x2="11" y2="5"/></svg>
            Date
          </div>
          <div class="detail-value">13/5/2018</div>
          <div class="detail-note">(Sunday)</div>
        </div>
        <div class="detail">
          <div class="detail-label">
            <svg viewBox="0 0 12 12" fill="none" stroke="currentColor" stroke-width="1.2"><circle cx="6" cy="6" r="5"/><polyline points="6,3 6,6 8,7"/></svg>
            Time
          </div>
          <div class="detail-value">2:00 pm</div>
          <div class="detail-note">(1:00 pm registration)</div>
        </div>
        <div class="detail">
          <div class="detail-label">
            <svg viewBox="0 0 12 12" fill="none" stroke="currentColor" stroke-width="1.2"><path d="M6 1a3 3 0 0 1 3 3c0 2-3 5-3 5S3 6 3 4a3 3 0 0 1 3-3z"/><line x1="2" y1="11" x2="10" y2="11"/></svg>
            Venue
          </div>
          <div class="detail-value">Merrowind Park,<br>Kestrel Quay</div>
        </div>
      </div>
    </aside>

    <div class="wreath" role="img" aria-label="Circular wreath of green leaves and red flowers"></div>
    <h1 class="title">
      <span class="title-line">Mother's Day</span>
      <span class="title-amp">&amp;</span>
      <span class="title-line">Baby Blessing</span>
    </h1>
    <div class="ceremony">Ceremony</div>

    <div class="photo" role="img" aria-label="Photograph of a long-haired mother kissing her smiling baby on the cheek, holding the baby in her arms"></div>

    <div class="logo">
      <div class="logo-mark"></div>
      <p class="logo-name">Lantern Meadow<br>Festival</p>
    </div>
  </main>
</body>
</html>
```